Toreva Cyber Security Capablties Brief

Design a 3 page that can stand alone or use one or two of the pages

This is capabilities brief for a company that does cyber and information security

Target Market(s)

Small to Large Companies

Industry/Entity Type

Cyber Security and Information Security

Font styles to use
Script

Requirements
Must have
• High tech look and feel, must staying in the Toreva Branding colors, expect for grapics

```html
<!DOCTYPE html>
<html lang="en">
<head>
<meta charset="utf-8">
<title>Toreva Capabilities Brief</title>
<link href="https://fonts.googleapis.com/css2?family=Orbitron:wght@800;900&family=Archivo+Narrow:wght@400;600;700&display=swap" rel="stylesheet">
<style>
:root{
  --canvas:#eef3f8;
  --navy-deep:#020a33;
  --navy:#0a1a4d;
  --blue:#0a4fc4;
  --blue-glow:#0aa2ff;
  --cyan:#3ef2f0;
  --cyan-soft:#5fe3f2;
  --label-blue:#1a6fb8;
  --ink:#0c1230;
  --body:#2b2f3f;
  --paper:#ffffff;
}
*{margin:0;padding:0;box-sizing:border-box}
html,body{width:1200px;height:1012px;overflow:hidden;background:var(--canvas)}
body{position:relative;font-family:"Archivo Narrow",Arial,sans-serif}
.page{position:absolute;top:163px;width:429px;height:616px;overflow:hidden;box-shadow:0 24px 50px rgba(20,30,60,.28)}
.page-cover{left:155px;background:radial-gradient(circle at 217px 307px,var(--blue-glow) 0%,#0565d8 22%,#0738a8 50%,var(--navy-deep) 100%)}
.page-inner{left:658px;background:var(--paper)}
.circuit-area{position:absolute;left:0;top:0}
.cover-title{position:absolute;top:92px;left:0;width:100%;text-align:center;font-family:"Orbitron",sans-serif;font-weight:900;font-size:22px;color:#fff;letter-spacing:-.5px}
.cover-intro{position:absolute;top:150px;left:60px;width:309px;text-align:center;color:#fff;font-size:7.6px;line-height:9px;text-transform:uppercase;letter-spacing:-.2px}
.cover-item{position:absolute;left:62px;display:flex;align-items:center;gap:10px}
.cover-item svg{width:34px;height:34px}
.cover-label{color:#fff;font-weight:700;font-size:8px;line-height:9px;text-transform:uppercase}
.band{position:absolute;left:0;top:0}
.inner-title{position:absolute;top:40px;left:0;width:100%;text-align:center;font-family:"Orbitron",sans-serif;font-weight:900;font-size:20px;line-height:27px;letter-spacing:-.6px;color:#fff}
.inner-title .accent{color:var(--cyan)}
.since{position:absolute;top:132px;right:31px;font-size:7.5px;font-weight:700;color:var(--label-blue)}
.lead-heading{position:absolute;top:174px;left:26px;font-size:10px;font-weight:700;color:var(--ink)}
.copy{position:absolute;left:26px;width:377px;font-size:7px;line-height:15.8px;color:var(--body);text-align:justify;text-align-last:justify}
.copy.last-free{text-align-last:left}
.feature{position:absolute;width:163px}
.feature-head{display:flex;align-items:center;gap:10px;height:34px}
.feature-head svg{width:34px;height:34px}
.feature-label{font-size:8px;line-height:9px;font-weight:600;color:var(--label-blue);text-transform:uppercase}
.feature-title{margin-top:8px;font-size:9.5px;font-weight:700;color:var(--ink)}
.feature-copy{margin-top:2px;font-size:7px;line-height:15.8px;color:var(--body);text-align:justify}
</style>
</head>
<body>

<section class="page page-cover">
  <svg class="circuit-area" width="429" height="616" role="img" aria-label="Glowing blue circuit board traces rising from the lower left to the right edge">
    <defs>
      <linearGradient id="circuitFill" x1="0" y1="1" x2="1" y2="0">
        <stop offset="0" stop-color="#0b2fa0" stop-opacity=".9"/>
        <stop offset=".5" stop-color="#1a5fe0" stop-opacity=".75"/>
        <stop offset="1" stop-color="#2a7cf0" stop-opacity=".5"/>
      </linearGradient>
    </defs>
    <polygon points="429,272 429,616 28,616 120,560 200,500 260,420 330,360" fill="url(#circuitFill)"/>
  </svg>

  <h1 class="cover-title">COMPANY HACKDAY</h1>
  <p class="cover-intro">Welcome to [Company Name], your trusted partner in cyber and information security. With our cutting-edge solutions and unparalleled expertise, we are dedicated to safeguarding your digital assets and protecting your organization from evolving threats.</p>

  <div class="cover-item" style="top:230px">
    <svg viewBox="0 0 34 34" role="img" aria-label="Hacker character at a laptop"><rect x="2" y="2" width="30" height="30" rx="6" fill="var(--cyan-soft)" opacity=".55"/></svg>
    <span class="cover-label">Network<br>Security</span>
  </div>
  <div class="cover-item" style="top:278px">
    <svg viewBox="0 0 34 34" fill="none" stroke="var(--cyan-soft)" stroke-width="1.8" stroke-linecap="round"><path d="M6 20a11 11 0 0 1 22-4"/><path d="M10 24a7 7 0 0 1 14-6"/><path d="M14 27a3 3 0 0 1 6-4"/><path d="M4 12a14 14 0 0 1 26 0"/></svg>
    <span class="cover-label">Network<br>Security</span>
  </div>
  <div class="cover-item" style="top:327px">
    <svg viewBox="0 0 34 34" fill="none" stroke="var(--cyan-soft)" stroke-width="2"><circle cx="17" cy="17" r="14" fill="var(--cyan-soft)" fill-opacity=".35"/><path d="M3 17h28M17 3c-6 8-6 20 0 28M17 3c6 8 6 20 0 28"/></svg>
    <span class="cover-label">Network<br>Security</span>
  </div>
  <div class="cover-item" style="top:376px">
    <svg viewBox="0 0 34 34" fill="none" stroke="var(--cyan-soft)" stroke-width="1.8" stroke-linejoin="round"><rect x="6" y="5" width="18" height="25" rx="2"/><rect x="11" y="3" width="8" height="4" rx="1"/><path d="M15 11v6M12 14h6"/><path d="M22 20l6 2v4c0 3-3 5-6 6-3-1-6-3-6-6v-4z" fill="var(--cyan-soft)"/><path d="M19 26l2 2 3-4" stroke="var(--navy)"/></svg>
    <span class="cover-label">Network<br>Security</span>
  </div>
</section>

<section class="page page-inner">
  <svg class="band" width="429" height="157">
    <defs>
      <linearGradient id="bandFill" x1="0" y1="0" x2="0" y2="1">
        <stop offset="0" stop-color="#071440"/>
        <stop offset="1" stop-color="var(--navy)"/>
      </linearGradient>
    </defs>
    <polygon points="0,0 429,0 429,104 0,156" fill="url(#bandFill)"/>
  </svg>
  <h2 class="inner-title"><span class="accent">TOGHETHER</span><br>IS MORE SECURE</h2>
  <p class="since">SINCE 2001</p>

  <h3 class="lead-heading">Welcome to [Company Name], your trusted partner</h3>
  <p class="copy" style="top:183px">Welcome to [Company Name], your trusted partner in cyber and information security. With our cutting-edge solutions and unparalleled expertise, we are dedicated to safeguarding your digital assets and protecting your organization from evolving threats. Welcome to [Company Name], your trusted partner in cyber and information security. With our cutting-edge solutions and unparalleled expertise, we are dedicated to safeguarding your digital assets and protecting your organization from evolving threats.</p>

  <div class="feature" style="left:45px;top:277px">
    <div class="feature-head">
      <svg viewBox="0 0 34 34" role="img" aria-label="Hacker character at a laptop"><rect x="2" y="2" width="30" height="30" rx="6" fill="var(--navy)" opacity=".2"/></svg>
      <span class="feature-label">Network<br>Security</span>
    </div>
    <h4 class="feature-title">Your trusted partner</h4>
    <p class="feature-copy">Rber and information security. With our cutting-edge solutions and unparalleled expertise, we are dedicated to safeguarding your digital assets and protecting your organization from evolving threats.</p>
  </div>

  <div class="feature" style="left:241px;top:277px">
    <div class="feature-head">
      <svg viewBox="0 0 34 34" fill="none" stroke="var(--navy)" stroke-width="1.8" stroke-linecap="round"><path d="M6 20a11 11 0 0 1 22-4"/><path d="M10 24a7 7 0 0 1 14-6"/><path d="M14 27a3 3 0 0 1 6-4"/><path d="M4 12a14 14 0 0 1 26 0"/></svg>
      <span class="feature-label">Network<br>Security</span>
    </div>
    <h4 class="feature-title">Your trusted partner</h4>
    <p class="feature-copy">Rber and information security. With our cutting-edge solutions and unparalleled expertise, we are dedicated to safeguarding your digital assets and protecting your organization from evolving threats.</p>
  </div>

  <div class="feature" style="left:45px;top:423px">
    <div class="feature-head">
      <svg viewBox="0 0 34 34" fill="none" stroke="var(--navy)" stroke-width="1.8" stroke-linejoin="round"><rect x="6" y="5" width="18" height="25" rx="2"/><rect x="11" y="3" width="8" height="4" rx="1"/><path d="M15 11v6M12 14h6"/><path d="M22 20l6 2v4c0 3-3 5-6 6-3-1-6-3-6-6v-4z" fill="var(--navy)"/><path d="M19 26l2 2 3-4" stroke="#fff"/></svg>
      <span class="feature-label">Network<br>Security</span>
    </div>
    <h4 class="feature-title">Your trusted partner</h4>
    <p class="feature-copy">Rber and information security. With our cutting-edge solutions and unparalleled expertise, we are dedicated to safeguarding your digital assets and protecting your organization from evolving threats.</p>
  </div>

  <div class="feature" style="left:241px;top:423px">
    <div class="feature-head">
      <svg viewBox="0 0 34 34" fill="none" stroke="var(--navy)" stroke-width="2"><circle cx="17" cy="17" r="14" fill="var(--navy)" fill-opacity=".85"/><path d="M3 17h28M17 3c-6 8-6 20 0 28M17 3c6 8 6 20 0 28" stroke="#fff" stroke-width="1.2"/></svg>
      <span class="feature-label">Network<br>Security</span>
    </div>
    <h4 class="feature-title">Your trusted partner</h4>
    <p class="feature-copy">Rber and information security. With our cutting-edge solutions and unparalleled expertise, we are dedicated to safeguarding your digital assets and protecting your organization from evolving threats.</p>
  </div>

  <p class="copy last-free" style="top:541px">and protecting your organization from evolving threats.</p>
  <p class="copy" style="top:557px">Welcome to [Company Name], your trusted partner in cyber and information security. With our cutting-edge solutions and unparalleled expertise, we are dedicated to safeguarding your digital assets and protecting your organization from evolving threats.</p>
</section>

</body>
</html>
```